Study Lantern

StudyLantern.com will be a place for people looking for information, resources, and advisement to start or continue their education. We want a friendly, inviting site design that makes finding what potential students are looking for simple and easy to navigate. We are not committed to the colors of the logo, so variations on the color scheme are welcome.

Text instructions based on the wireframe: For the site's homepage we'd like a banner at the very top for our Logo and white space to the right of it. See attachments for logo + wireframe. Below that would be navigation. Below that split into 2/3 on the left we would have home page content, and 1/3 on the right we would have the lead form. At the bottom of the page we would have a space for types of degrees, then a footer with copyright info + site info.

See wireframes for additional page layouts.

Industry/Entity Type

Education

Requirements
Must have
• At minimum we are looking for three pages: homepage, choose your degree path page, and content page.
Nice to have
• -White space is appreciated
-Variations on the color scheme are welcome, we are not married to the existing logo's color scheme.

```html
<!DOCTYPE html>
<html lang="en">
<head>
<meta charset="utf-8">
<title>StudyLantern.com</title>
<link href="https://fonts.googleapis.com/css2?family=Arimo:ital,wght@0,400;0,700;1,400&family=Anton&family=Open+Sans:wght@600&display=swap" rel="stylesheet">
<style>
:root{
  --green:#7eac2b;
  --green-dark:#4f7a17;
  --green-text:#78a82a;
  --orange:#f26a1b;
  --orange-light:#f9a21b;
  --ink:#2c3a44;
  --body:#444;
  --muted:#666;
  --page:#e4e4e4;
  --panel:#f6f6f6;
  --white:#fff;
  --yellow:#ffee22;
}
*{margin:0;padding:0;box-sizing:border-box}
html,body{width:1200px;height:1151px;overflow:hidden}
body{position:relative;font-family:Arimo,Arial,sans-serif;color:var(--body);
  background:linear-gradient(#fff 0,#ededed 137px,var(--page) 137px,var(--page) 862px,var(--panel) 866px,#ececec 1151px)}
.abs{position:absolute}
.top-tab{left:822px;top:0;width:192px;height:30px;background:var(--green);border-radius:0 0 7px 7px;color:#fff;font-size:12px;display:flex;align-items:center;padding-left:20px;white-space:nowrap}
.top-tab span{margin-right:26px}
.top-tab .sep{margin:0 8px}
.brand{left:159px;top:52px;display:flex;align-items:center;gap:12px;font-family:"Open Sans",sans-serif;font-weight:600;font-size:42px;color:var(--ink);letter-spacing:-0.5px}
.brand i{display:block;width:30px;height:30px;background:var(--orange)}
.social{top:93px;width:30px;height:30px;border-radius:50%;background:#fff;border:1px solid #ddd;box-shadow:0 1px 2px rgba(0,0,0,.15)}
.nav{left:0;top:137px;width:1200px;height:48px;background:var(--green)}
.nav a{position:absolute;top:16px;color:#fff;text-decoration:none;font-size:13.5px;letter-spacing:.3px;white-space:nowrap}
.search{left:755px;top:142px;width:246px;height:40px;background:#fff;border:1px solid #cfd8c0;border-radius:3px 0 0 3px}
.go{left:1001px;top:142px;width:42px;height:40px;background:linear-gradient(var(--orange-light),var(--orange));color:#fff;font-size:18px;display:flex;align-items:center;justify-content:center;border-radius:0 3px 3px 0}
.slider{left:150px;top:185px;width:900px;height:158px;background:#f5f5f5;border:1px solid #d6d6d6;border-top:none;border-radius:0 0 8px 8px}
.arrow{top:244px;width:38px;height:38px;border-radius:50%;background:linear-gradient(#fff,#e2e2e2);border:1px solid #bbb}
.divider{left:553px;top:206px;width:1px;height:121px;background:#ccc}
.welcome{left:213px;top:228px;font-size:23px;color:var(--orange)}
.site-title{left:213px;top:257px;font-size:36px;font-weight:700;color:var(--ink);white-space:nowrap}
.invest{left:583px;top:206px;font-size:22px;color:var(--orange);white-space:nowrap}
.question{left:584px;top:241px;font-size:13.5px;color:var(--green-text);white-space:nowrap}
.blurb{left:585px;top:266px;width:390px;font-size:11.5px;line-height:17px;color:var(--muted);letter-spacing:.2px}
.tagline{left:585px;top:311px;font-size:14px;font-style:italic;color:var(--ink);white-space:nowrap}
.shadow{top:790px;height:25px;width:1000px;left:125px;background:radial-gradient(ellipse at 50% 100%,rgba(0,0,0,.25),transparent 70%)}
.card{left:154px;top:384px;width:603px;height:431px;background:linear-gradient(#fff,#f2f2f2);border:1px solid #ccc;border-radius:8px 0 0 8px}
.card h2{position:absolute;left:16px;top:18px;font-weight:400;font-size:20px;color:var(--green-text)}
.card hr{position:absolute;left:16px;top:55px;width:547px;border:none;border-top:1px solid #d8d8d8}
.card p{position:absolute;left:16px;width:547px;font-size:12px;line-height:22.5px;text-align:justify;text-indent:34px;color:#444}
.btn-more{height:27px;border-radius:14px;background:linear-gradient(#fff,#ddd);border:1px solid #c9c9c9;box-shadow:0 1px 2px rgba(0,0,0,.2);font-size:12px;color:#555;display:flex;align-items:center;justify-content:space-between;padding:0 6px 0 13px;white-space:nowrap}
.btn-more svg{width:17px;height:17px;flex-shrink:0}
.form{left:755px;top:368px;width:290px;height:447px;background:linear-gradient(#7eae2c,#4d7d18);border:1px solid #3f6a10;border-radius:8px;color:#fff}
.form h3{position:absolute;left:9px;top:10px;font-family:Anton,Impact,sans-serif;font-weight:400;font-size:25px;line-height:34px;white-space:nowrap;text-shadow:0 1px 2px rgba(0,0,0,.4)}
.form .intro{position:absolute;left:10px;top:50px;width:272px;font-size:12px;line-height:17px}
.form .match{position:absolute;left:10px;top:86px;font-size:13.5px;color:var(--yellow);white-space:nowrap}
.form .req{position:absolute;left:100px;top:119px;font-size:8px;letter-spacing:1px;color:var(--yellow);white-space:nowrap}
.form label{position:absolute;left:10px;font-size:11.5px;line-height:13px;white-space:nowrap}
.field{position:absolute;left:103px;width:176px;height:21px;background:linear-gradient(#fff,#ececec);border:1px solid #c7c7c7;border-radius:3px}
.field.select::after{content:"";position:absolute;right:2px;top:2px;width:16px;height:15px;background:linear-gradient(#ddd,#bbb);border-radius:2px}
.field.select::before{content:"";position:absolute;right:6px;top:7px;z-index:1;border-left:4px solid transparent;border-right:4px solid transparent;border-top:6px solid #777}
.submit{position:absolute;left:103px;top:400px;width:176px;height:37px;background:linear-gradient(#ffc640,#f08a0f);border:1px solid #b85a00;border-radius:5px;font-family:Anton,Impact,sans-serif;font-size:19px;color:#8a3a05;display:flex;align-items:center;justify-content:center;white-space:nowrap}
.privacy{left:755px;top:820px;width:290px;text-align:center;font-size:11px;line-height:13px;color:#333}
.rule{left:0;top:862px;width:1200px;height:4px;background:var(--green)}
.foot-title{top:886px;font-size:12px;font-weight:700;color:var(--green-text)}
.degree{width:175px;height:34px;border-bottom:1px dotted #aaa;font-size:12px;color:#333;display:flex;align-items:center;padding-left:34px;position:absolute;white-space:nowrap}
.degree::before{content:"";position:absolute;left:2px;top:10px;width:13px;height:13px;border-radius:50%;background:linear-gradient(#fff,#ddd);border:1px solid #c4c4c4}
.degree::after{content:"";position:absolute;left:8px;top:14px;border-top:3px solid transparent;border-bottom:3px solid transparent;border-left:4px solid #777}
.foot-copy{left:829px;top:915px;width:214px;font-size:12px;line-height:17px;text-align:justify;color:#333}
.copyright{left:0;top:1100px;width:1200px;text-align:center;font-size:12px;letter-spacing:.6px;color:#222}
</style>
</head>
<body>
<div class="abs top-tab"><span>F.A.Q.</span>Login<span class="sep">I</span>Register</div>
<div class="abs brand"><span>studylantern</span><i></i></div>
<div class="abs social" style="left:919px"></div>
<div class="abs social" style="left:965px"></div>
<div class="abs social" style="left:1011px"></div>

<nav class="abs nav">
  <a style="left:163px">Home</a><a style="left:231px">About Us</a><a style="left:320px">Feedback</a>
  <a style="left:413px">Privacy Policy</a><a style="left:534px">Terms of Use</a><a style="left:651px">Contact Us</a>
</nav>
<div class="abs search"></div>
<div class="abs go">Go</div>

<section class="abs slider"></section>
<div class="abs arrow" style="left:156px"><svg width="36" height="36" viewBox="0 0 36 36"><path d="M22 10 12 18l10 8z" fill="#777"/></svg></div>
<div class="abs arrow" style="left:1008px"><svg width="36" height="36" viewBox="0 0 36 36"><path d="M14 10l10 8-10 8z" fill="#777"/></svg></div>
<div class="abs divider"></div>
<div class="abs welcome">WELCOME TO</div>
<div class="abs site-title">StudyLantern.com</div>
<div class="abs invest">Invest In Your Future Today</div>
<div class="abs question">Are you overwhelmed by the thought of choosing the right college?</div>
<div class="abs blurb">StudyLantern helps simplify this process by matching colleges to you and your needs. Tell us about yourself and let us do the work for you.</div>
<div class="abs tagline">Take control of your future by furtheing your education.</div>

<div class="abs shadow"></div>
<article class="abs card">
  <h2>About StudyLantern</h2>
  <hr>
  <p style="top:84px">StudyLantern.com is a free resource to start your path to a college degree and compare higher education options that can generally lead to improved career or job opportunities based on numerous employment reports from organizations like the National Labor Statistics Office. Our free education tools and resources do not guarantee employment nor an offer of employment.</p>
  <p style="top:196px">Our mission is to match you with the top colleges, universities or technical institutions that offer the higher education programs that meet your goals, based on the information you provided. Enrollment and Education Experts at the Private &amp; Public Institutions we partner with can provide you with additional, detailed information on a) applying for their school b) tuition costs and tuition assistance for their school and c) career and employment information and statistics for students that have successfully completed programs in that field or from their particular school.</p>
  <div class="abs btn-more" style="left:446px;top:349px;width:104px">Read more <svg viewBox="0 0 17 17"><circle cx="8.5" cy="8.5" r="8" fill="#6fa421"/><path d="M4 8.5h7M8 5l3.5 3.5L8 12" stroke="#fff" stroke-width="2" fill="none"/></svg></div>
</article>

<form class="abs form">
  <h3>Tell us more about YOU!</h3>
  <div class="intro">StudyLantern provides you with accredite school information that match your interests.</div>
  <div class="match">Get matched to the right schools today.</div>
  <div class="req">*Required fields</div>
  <label style="top:135px">Subject*</label><div class="field select" style="top:131px"></div>
  <label style="top:163px">Degree Level*</label><div class="field select" style="top:159px"></div>
  <label style="top:191px">High School<br>Grad Yr.*</label><div class="field select" style="top:187px"></div>
  <label style="top:232px">First Name*</label><div class="field" style="top:228px"></div>
  <label style="top:260px">Last Name*</label><div class="field" style="top:256px"></div>
  <label style="top:288px">Street Address*</label><div class="field" style="top:284px"></div>
  <label style="top:316px">Zip / City / State*</label>
  <div class="field" style="top:312px;width:52px"></div>
  <div class="field" style="top:312px;left:158px;width:66px"></div>
  <div class="field" style="top:312px;left:227px;width:52px"></div>
  <label style="top:344px">Phone Number*</label><div class="field" style="top:340px"></div>
  <label style="top:372px">Email Address*</label><div class="field" style="top:368px"></div>
  <div class="submit">Request Information</div>
</form>
<div class="abs privacy">Your information will be kept strictly private as<br>stated in our Privacy Policy.</div>

<div class="abs rule"></div>
<div class="abs foot-title" style="left:157px">Types of Degree</div>
<div class="degree" style="left:156px;top:909px">Degree Type One here</div>
<div class="degree" style="left:156px;top:943px">Degree Type Two here</div>
<div class="degree" style="left:156px;top:977px">Degree Type Three here</div>
<div class="degree" style="left:156px;top:1011px">Degree Type Four here</div>
<div class="degree" style="left:381px;top:909px">Degree Type Five here</div>
<div class="degree" style="left:381px;top:943px">Degree Type Six here</div>
<div class="degree" style="left:381px;top:977px">Degree Type Seven here</div>
<div class="degree" style="left:381px;top:1011px">Degree Type Eight here</div>
<div class="degree" style="left:605px;top:909px">Degree Type Nine here</div>
<div class="degree" style="left:605px;top:943px">Degree Type Ten here</div>
<div class="degree" style="left:605px;top:977px">Degree Type Elevent here</div>
<div class="degree" style="left:605px;top:1011px">Degree Type One here</div>

<div class="abs foot-title" style="left:829px">Degree Content?</div>
<div class="abs foot-copy">Duis autem vel eum iriure dolor in hendrerit in vulputate velit esse molestie consequat, vel illum dolore eu feugiat nulla facilisis at vero eros et accumsan et iusto odio dignissim qui blandit praesent luptatum zzril delenit.</div>
<div class="abs btn-more" style="left:939px;top:1028px;width:104px">Read more <svg viewBox="0 0 17 17"><circle cx="8.5" cy="8.5" r="8" fill="#6fa421"/><path d="M4 8.5h7M8 5l3.5 3.5L8 12" stroke="#fff" stroke-width="2" fill="none"/></svg></div>

<div class="abs copyright">© Copyright 2009-2012 StudyLantern.com™ &amp; Northfield Learning, Inc. All Rights Reserved.</div>
</body>
</html>
```